Book cover for a book on tactics, habits and directives learned from world class performers

The Quiet Ledger book is the first in a series of four books filled with proven tactics, habits and directives (i.e., what to do) that young, ambitious working professionals should be doing to make their life better. The first book is on foundational or keystone habits - that is, the habits that will help everyone upgrade their life and enable other great habits in their life (things such as waking up early in the morning or exercising)

The goal of the book is to stand out on the Brimvale platform as a small thumbnail, as well as a 5 x 8 book.

The imagery should make the viewer feel that the book (and the author) are the authority in habits and developing habits.

The reader should feel that they must have this book if they know they should be developing successful habits but do not want to comb through hundreds of books just to find the one tactic or habit that they should be doing. It's important that the book "pops off the shelf" and catches the eye quickly.

The most important part of the design is that it sells, not that it looks well-designed. I am open to any image or illustration you choose though please consider the nice have I have listed below. Here are a few words that come to mind when thinking of my book: growth, self development, leadership, success, freedom, passion, motivation, young professional, accomplished, experience.

I like a bold color palette. I like bold titles that you know right away what the title is and what it is about, not too busy and with simple color schemes. 2 - 3 colors.

Books with covers I like:
- Lamp Orchard by Norris Pellaquin
- Under The Copper Tide by Gordon Pruitt
- The Velvet Compass by Edgar Fulbright

Target Market(s)

- Young 20 - 40 year old ambitious working professionals interested in self development and listen to podcasts of Ned Caplow, Rufus Denholme
- Just starting out management consultants

Colors

Designer to choose colors to be used in the design.

Requirements
Must have
• 'Quiet Ledger' title - first and foremost
• Author name - Lu Qiao - probably on the bottom or somewhere
• Bold colour / colours or a graphic that is eye catching (and makes it different from other habits books on Brimvale)
Nice to have
• Would like to have some sort of visual, colour or theme that can run through the four books - would be great to have a cover design that can be simply changed to depict the second, third or fourth book in the series - maybe the graphic or visual can be changed with some colours, etc. but with the overall feel looking similar so that people can see that it's part of the same book series

```html
<!DOCTYPE html>
<html lang="en">
<head>
<meta charset="utf-8">
<title>Quiet Ledger — Lu Qiao</title>
<link href="https://fonts.googleapis.com/css2?family=Oswald:wght@400;600&display=swap" rel="stylesheet">
<style>
  :root {
    --page: #ffffff;
    --cover-top: #72d1e6;
    --cover-bottom: #62c1db;
    --cover-mid: #93d4e3;
    --title-blue: #1c4f8c;
    --author-ink: #2a2a2a;
    --boat-red: #e2363d;
    --boat-white: #eaf0f5;
    --trail: #1f3440;
  }
  * { margin: 0; padding: 0; box-sizing: border-box; }
  html, body {
    width: 1200px;
    height: 1200px;
    overflow: hidden;
    background: var(--page);
  }
  .canvas {
    position: relative;
    width: 1200px;
    height: 1200px;
  }
  .cover {
    position: absolute;
    left: 275px;
    top: 50px;
    width: 651px;
    height: 1100px;
    overflow: hidden;
    background:
      radial-gradient(ellipse at 75% 45%, var(--cover-mid) 0%, rgba(147,212,227,0) 60%),
      linear-gradient(180deg, var(--cover-top) 0%, var(--cover-bottom) 100%);
  }
  .author {
    position: absolute;
    top: 26px;
    left: 0;
    width: 100%;
    text-align: center;
    font-family: "Oswald", sans-serif;
    font-weight: 400;
    font-size: 48px;
    letter-spacing: 0.32em;
    padding-left: 0.32em;
    color: var(--author-ink);
    line-height: 1;
  }
  .title {
    position: absolute;
    top: 112px;
    left: 0;
    width: 100%;
    text-align: center;
    font-family: "Oswald", sans-serif;
    font-weight: 600;
    font-size: 142px;
    line-height: 0.92;
    letter-spacing: 0.01em;
    color: var(--title-blue);
    text-transform: uppercase;
  }
  .title span { display: block; }
  .trails {
    position: absolute;
    left: 0;
    top: 0;
    width: 651px;
    height: 1100px;
  }
  .boat {
    position: absolute;
    border-radius: 6px;
  }
  .boat--lead {
    left: 283px; top: 405px; width: 119px; height: 127px;
    background: var(--boat-red);
  }
  .boat--one {
    left: 283px; top: 748px; width: 163px; height: 119px;
    background: var(--boat-white);
  }
  .boat--two {
    left: 84px; top: 884px; width: 159px; height: 110px;
    background: var(--boat-white);
  }
  .boat--three {
    left: 415px; top: 959px; width: 186px; height: 123px;
    background: var(--boat-white);
  }
</style>
</head>
<body>
<main class="canvas">
  <section class="cover">
    <p class="author">LU QIAO</p>
    <h1 class="title"><span>Quiet</span><span>Ledger</span></h1>

    <svg class="trails" viewBox="0 0 651 1100" aria-hidden="true">
      <g fill="none" stroke="var(--trail)" stroke-width="2.5" stroke-linecap="round" stroke-dasharray="0 8">
        <path d="M13 695 C 130 640, 230 600, 286 530"/>
        <path d="M13 800 L 285 802"/>
        <path d="M8 935 L 86 936"/>
        <path d="M8 993 C 150 995, 300 1005, 418 1016"/>
      </g>
    </svg>

    <div class="boat boat--lead" role="img" aria-label="Red folded paper boat sailing ahead, leading the group"></div>
    <div class="boat boat--one" role="img" aria-label="White folded paper boat"></div>
    <div class="boat boat--two" role="img" aria-label="White folded paper boat"></div>
    <div class="boat boat--three" role="img" aria-label="White folded paper boat"></div>
  </section>
</main>
</body>
</html>
```